Brell Harbor Company Business Cards

Front and Back Business Card - logo and text setup - cool design. I need workable photoshop or illustrator files so I can setup each employee card with design that is created
Updates

Hi everyone, thank you for the great entries. Please no more white and blue cards - there are so many already - black and silver only now please. thanks!

Target Market(s)

Construction Industry - Facility Managers

Industry/Entity Type

Construction

Contact Information for Business Card

I really like contemporary simplistic looks - clean neat....not opposed to seeing some black backrounds

Requirements
Must have
• Logo/website address with design on front only - www.brellharbor-example.com (logo attached)
• Back:
• Name/Title/Company Address/Phone/email address
Nice to have
• Cool design
Should not have
• Nothing gimmicky like Fire or Water - since we are a Fire Protection company - it has all been done

```html
<!DOCTYPE html>
<html lang="en">
<head>
<meta charset="utf-8">
<title>Brell Harbor Company – Business Cards</title>
<link href="https://fonts.googleapis.com/css2?family=Roboto:wght@400;700&display=swap" rel="stylesheet">
<style>
  :root {
    --page-bg: #e6e6e4;
    --card-black: #1b1c1e;
    --card-silver: #dcdde0;
    --silver: #c3c6cb;
    --silver-soft: #8e9298;
    --ink-black: #141517;
    --ink-grey: #4a4d52;
    --rule-grey: #9a9ea4;
  }
  * { margin: 0; padding: 0; box-sizing: border-box; }
  html, body {
    width: 1125px; height: 1200px; overflow: hidden;
    background: var(--page-bg);
    font-family: "Roboto", Arial, sans-serif;
  }
  .canvas { position: relative; width: 1125px; height: 1200px; }
  .card { position: absolute; left: 156px; width: 825px; height: 471px; }
  .card--front { top: 106px; background: var(--card-black); }
  .card--back { top: 639px; background: var(--card-silver); }

  .wordmark {
    position: absolute; left: 0; right: 0; top: 170px;
    display: flex; align-items: center; justify-content: center; gap: 18px;
    font-weight: 700; font-size: 74px; letter-spacing: -1px; line-height: 1;
    color: var(--silver);
  }
  .wordmark__square { width: 26px; height: 26px; background: var(--silver); }
  .website {
    position: absolute; left: 0; right: 0; top: 270px;
    text-align: center; font-size: 20px; letter-spacing: 2px;
    color: var(--silver-soft);
  }

  .divider { position: absolute; left: 45px; top: 150px; width: 735px; height: 2px; background: var(--rule-grey); }
  .divider__accent { position: absolute; left: 0; top: -1px; width: 209px; height: 4px; background: var(--ink-black); }

  .person { position: absolute; left: 47px; top: 178px; }
  .person__name { font-weight: 700; font-size: 31px; color: var(--ink-black); line-height: 1.1; }
  .person__title { font-size: 21px; color: var(--ink-grey); line-height: 1.3; }
  .person__address { margin-top: 10px; font-size: 20px; color: var(--ink-grey); line-height: 1.3; }

  .contacts { position: absolute; right: 45px; top: 186px; list-style: none; }
  .contacts li {
    display: flex; align-items: center; justify-content: flex-end; gap: 12px;
    font-size: 20px; color: var(--ink-grey); height: 30px;
  }
  .contacts svg { width: 18px; height: 18px; fill: var(--ink-black); flex: none; }
</style>
</head>
<body>
<div class="canvas">

  <section class="card card--front">
    <div class="wordmark"><span>Brell Harbor</span><span class="wordmark__square"></span></div>
    <p class="website">www.brellharbor-example.com</p>
  </section>

  <section class="card card--back">
    <div class="divider"><div class="divider__accent"></div></div>

    <div class="person">
      <p class="person__name">Dana Whitlow</p>
      <p class="person__title">CEO/Founder</p>
      <p class="person__address">48 Quarry Lane<br>Northfield, ST 00000</p>
    </div>

    <ul class="contacts">
      <li>(555) 014-2290
        <svg viewBox="0 0 24 24"><path d="M6.6 10.8a15.1 15.1 0 0 0 6.6 6.6l2.2-2.2c.3-.3.7-.4 1-.2 1.1.4 2.3.6 3.6.6.6 0 1 .4 1 1V20c0 .6-.4 1-1 1A17 17 0 0 1 3 4c0-.6.4-1 1-1h3.5c.6 0 1 .4 1 1 0 1.3.2 2.5.6 3.6.1.3 0 .7-.2 1z"/></svg>
      </li>
      <li>(555) 014-2291
        <svg viewBox="0 0 24 24"><path d="M6 2h9l3 3v4H6z"/><path d="M2 10h20v8h-3v-3H5v3H2z"/><path d="M6 16h12v6H6z"/></svg>
      </li>
      <li>info@brellharbor-example.com
        <svg viewBox="0 0 24 24"><path d="M2 5h20v14H2z M4 7v.5l8 5 8-5V7z" fill-rule="evenodd"/></svg>
      </li>
    </ul>
  </section>

</div>
</body>
</html>
```